Banner Designs for Drone Defense Ad Campaign

Corvane is a security consulting and services company that offers a service called SkyMindful. SkyMindful helps our customers identify security risks from drones and develops comprehensive protection programs. We are looking for a designer to create a banner ad in three sizes for our campaign.
Target Market(s)
Our campaign is geared to the sports and entertainment industry, specifically large event venues and their security operation.
Industry/Entity Type
Security
Font styles to use
Other font styles liked:
- Raleway
Requirements
Must have
- Banner Objective
The visual and textual content of the banner should prompt the viewer to quickly identify the service offered and the information that is available to download.
Banner Design
Logo: SkyMindful logo
Call to Action Button in Red: Get It Here (On Right or or Upper Right)
Title in Larger Font: Guide to UAS Risk Mitigation
Subtitle in smaller Font: 5 Steps to Develop Your Comprehensive UAS Defense Program
Background: Stadium with a drone flying in foreground
Font: Raleway
Banner Sizes
1 - 1200x670 pixels
2 - 1510x196 pixels
3 - 1200x628 pixels

```html
<!DOCTYPE html>
<html lang="en">
<head>
<meta charset="utf-8">
<title>SkyMindful – Guide to UAS Risk Mitigation</title>
<link rel="stylesheet" href="https://fonts.googleapis.com/css2?family=Raleway:wght@400;500;600&family=Rubik:wght@800;900&display=swap">
<style>
  :root {
    --brand-blue: #3f86e6;
    --title-blue: #3a82f0;
    --ink: #2b2b2b;
    --cta-red: #ff3b1f;
    --cta-light: #ff8a73;
    --accent-red: #ff2a0a;
    --sky-top: #ffffff;
    --sky-bottom: #7dd2f7;
    --drone-light: #e4e6e8;
    --drone-mid: #a9adb2;
  }
  * { margin: 0; padding: 0; box-sizing: border-box; }
  html, body { width: 1200px; height: 670px; overflow: hidden; }
  body { font-family: "Raleway", sans-serif; }

  .banner {
    position: relative;
    width: 1200px;
    height: 670px;
    overflow: hidden;
    background: linear-gradient(160deg, var(--sky-top) 0%, #eaf7fd 35%, #bfe8fb 70%, var(--sky-bottom) 100%);
  }

  .accent-glow {
    position: absolute;
    left: 560px;
    top: 120px;
    width: 700px;
    height: 600px;
    background: radial-gradient(ellipse at 70% 70%, rgba(255, 42, 10, 0.35) 0%, rgba(255, 42, 10, 0.12) 45%, rgba(255, 42, 10, 0) 70%);
  }

  .brand {
    position: absolute;
    left: 118px;
    top: 150px;
    color: var(--brand-blue);
  }
  .brand-name {
    font-size: 58px;
    font-weight: 500;
    letter-spacing: -0.5px;
    line-height: 1;
  }
  .brand-by {
    margin-top: 14px;
    margin-left: 184px;
    font-size: 28px;
    font-weight: 500;
    color: var(--ink);
  }

  .cta {
    position: absolute;
    left: 684px;
    top: 60px;
    width: 382px;
    height: 76px;
    border-radius: 38px;
    background: linear-gradient(180deg, var(--cta-light) 0%, var(--cta-red) 55%, #f02a10 100%);
    color: #fff;
    font-family: "Rubik", sans-serif;
    font-weight: 800;
    font-size: 38px;
    letter-spacing: 0.5px;
    text-transform: uppercase;
    display: flex;
    align-items: center;
    justify-content: center;
    text-decoration: none;
  }

  .drone-art {
    position: absolute;
    left: 648px;
    top: 180px;
    width: 520px;
    height: 345px;
    border-radius: 40px;
    background: radial-gradient(ellipse at 55% 45%, var(--drone-light) 0%, var(--drone-mid) 70%, rgba(169,173,178,0.6) 100%);
  }

  .title {
    position: absolute;
    left: 80px;
    top: 302px;
    font-family: "Rubik", sans-serif;
    font-weight: 900;
    font-size: 70px;
    line-height: 82px;
    color: var(--title-blue);
    letter-spacing: 0.3px;
    text-shadow:
      -3px -3px 0 #fff, 3px -3px 0 #fff, -3px 3px 0 #fff, 3px 3px 0 #fff,
      0 -3px 0 #fff, 0 3px 0 #fff, -3px 0 0 #fff, 3px 0 0 #fff,
      5px 6px 6px rgba(0,0,0,0.25);
  }

  .subtitle {
    position: absolute;
    left: 88px;
    top: 497px;
    display: flex;
    gap: 24px;
    font-size: 41px;
    font-weight: 400;
    line-height: 46px;
    color: var(--ink);
  }
  .subtitle-arrow { flex: none; margin-top: 17px; }
</style>
</head>
<body>
  <main class="banner">
    <div class="accent-glow" role="img" aria-label="Red curved accent bands sweeping up behind the drone"></div>

    <div class="brand">
      <div class="brand-name">SkyMindful</div>
      <div class="brand-by">By Corvane</div>
    </div>

    <a class="cta" href="#">Get It Here</a>

    <div class="drone-art" role="img" aria-label="Illustration of a white quadcopter drone with a camera gimbal"></div>

    <h1 class="title">Guide to UAS Risk<br>Mitigation</h1>

    <p class="subtitle">
      <svg class="subtitle-arrow" width="26" height="16" viewBox="0 0 26 16" aria-hidden="true">
        <path d="M0 8 H22 M15 1 L23 8 L15 15" fill="none" stroke="var(--accent-red)" stroke-width="3"/>
      </svg>
      <span>5 Steps to Develop Your<br>Comprehensive UAS Defense Program</span>
    </p>
  </main>
</body>
</html>
```